Business Cards for Live Events Company

We are Flumo's.
We are Looking for a business card design for our live entertainment technical company.
We design lighting, video, and audio for Theatre, Live events, and Concerts.

We also hire out technical equipment for these, which includes: Lights, Special FX, Audio, Video, Projection, LED Screens, Rigging, Staging.

Have a look at our website and Facebook page for an idea of what we do.
www.flumos.com.au www.facebook.com/flumosproductions

Be creative with the design, we are looking for something eye catching.

included are 4 different styles of our logo which we use. Take your pick of what you prefer.

Industry/Entity Type

Events

Font styles to use
Serif
Sans Serif
Script

Requirements
Must have
• Eye catching, we are a design company creative events.
all the usual contact details etc.
Nice to have
• good use of colour
Should not have
• Nothing really....

```html
<!DOCTYPE html>
<html lang="en">
<head>
<meta charset="utf-8">
<title>Flumo's Business Card</title>
<link rel="stylesheet" href="https://fonts.googleapis.com/css2?family=Josefin+Sans:wght@300;400;700&family=Comfortaa:wght@400&display=swap">
<style>
  :root {
    --page-bg: #6a6a6a;
    --navy-deep: #0a1428;
    --navy-mid: #12305a;
    --navy-glow: #1b4a80;
    --teal: #2fc6d6;
    --cyan: #1fa8e8;
    --cyan-bright: #2ec2ff;
    --silver: #c9ced6;
    --silver-dark: #7d8592;
    --white-soft: #e8eef5;
  }
  html, body {
    margin: 0;
    padding: 0;
    width: 1200px;
    height: 473px;
    overflow: hidden;
    background: var(--page-bg);
  }
  .sheet {
    position: relative;
    width: 1200px;
    height: 473px;
  }
  .card {
    position: absolute;
    top: 82px;
    width: 491px;
    height: 280px;
    overflow: hidden;
    background:
      radial-gradient(ellipse at 50% 45%, var(--navy-glow) 0%, var(--navy-mid) 40%, var(--navy-deep) 100%);
  }
  .card--front { left: 60px; }
  .card--back  { left: 648px; }

  /* Front */
  .front-glow {
    position: absolute;
    left: 76px;
    top: 2px;
    width: 340px;
    height: 270px;
    border-radius: 50%;
    background: radial-gradient(ellipse at center, rgba(47,198,214,0.55) 0%, rgba(47,198,214,0.25) 40%, rgba(47,198,214,0) 70%);
  }
  .front-emblem {
    position: absolute;
    left: 155px;
    top: 46px;
    width: 182px;
    height: 182px;
    box-sizing: border-box;
    border-radius: 50%;
    border: 8px solid var(--silver);
    box-shadow: 0 0 0 1px var(--silver-dark), inset 0 0 0 1px var(--silver-dark);
    background: radial-gradient(circle at 50% 40%, #1c3d63 0%, #142c4b 100%);
    display: flex;
    align-items: center;
    justify-content: center;
  }
  .brand-name {
    font-family: "Josefin Sans", sans-serif;
    font-weight: 700;
    color: var(--silver);
    font-size: 34px;
    letter-spacing: 1px;
    line-height: 1;
  }
  .front-url {
    position: absolute;
    left: 0;
    right: 0;
    top: 250px;
    text-align: center;
    font-family: "Josefin Sans", sans-serif;
    font-weight: 300;
    font-size: 12px;
    letter-spacing: 6.2px;
    color: var(--white-soft);
  }

  /* Back */
  .holder-name {
    position: absolute;
    left: 28px;
    top: 50px;
    margin: 0;
    font-family: "Josefin Sans", sans-serif;
    font-size: 31px;
    font-weight: 400;
    color: var(--cyan);
    line-height: 1;
    white-space: nowrap;
  }
  .holder-name strong { font-weight: 700; }
  .holder-role {
    position: absolute;
    left: 29px;
    top: 82px;
    margin: 0;
    font-family: "Josefin Sans", sans-serif;
    font-size: 16px;
    color: var(--cyan);
    line-height: 1;
  }
  .contact-list {
    position: absolute;
    left: 33px;
    top: 139px;
    margin: 0;
    padding: 0;
    list-style: none;
  }
  .contact-item {
    display: flex;
    align-items: center;
    height: 24.5px;
  }
  .contact-icon {
    width: 34px;
    height: 22px;
    flex: none;
  }
  .contact-text {
    margin-left: 15px;
    font-family: "Comfortaa", sans-serif;
    font-size: 14px;
    color: var(--cyan);
    white-space: nowrap;
  }
  .back-brand {
    position: absolute;
    left: 323px;
    top: 0;
    width: 168px;
    height: 280px;
    display: flex;
    align-items: center;
    justify-content: center;
  }
  .back-brand .brand-name {
    color: var(--cyan-bright);
    font-size: 38px;
  }
</style>
</head>
<body>
<main class="sheet">

  <section class="card card--front" aria-label="Card front">
    <div class="front-glow" role="img" aria-label="Teal halftone dot burst around the emblem"></div>
    <div class="front-emblem">
      <span class="brand-name">Flumo's</span>
    </div>
    <p class="front-url">WWW.LOREMIPSUM.COM</p>
  </section>

  <section class="card card--back" aria-label="Card back">
    <h1 class="holder-name"><strong>NAME</strong> SURNAME</h1>
    <p class="holder-role">LOREM IPSUM</p>

    <ul class="contact-list">
      <li class="contact-item">
        <svg class="contact-icon" viewBox="0 0 34 22" fill="none" stroke="#1fa8e8" stroke-width="1.4">
          <circle cx="11" cy="11" r="9.5"/>
          <path d="M21 11h12M33 3v16"/>
          <path d="M7.5 6.5c.8-.8 1.6-.6 2 .2l1 1.8c.3.6 0 1.1-.5 1.5-.4.3-.3.8 0 1.3.6 1 1.4 1.8 2.4 2.4.5.3 1 .4 1.3 0 .4-.5.9-.8 1.5-.5l1.8 1c.8.4 1 1.2.2 2-1.3 1.3-3.4 1-6-1.2-2.8-2.4-4.5-5.2-3.7-8.5z" fill="#1fa8e8" stroke="none"/>
        </svg>
        <span class="contact-text">12345 54321</span>
      </li>
      <li class="contact-item">
        <svg class="contact-icon" viewBox="0 0 34 22" fill="none" stroke="#1fa8e8" stroke-width="1.4">
          <circle cx="11" cy="11" r="9.5"/>
          <path d="M21 11h12M33 3v16"/>
          <rect x="6" y="7.5" width="10" height="7" fill="#1fa8e8" stroke="none"/>
          <path d="M6 7.5l5 4 5-4" stroke="#0a1428" stroke-width="1"/>
        </svg>
        <span class="contact-text">loremipsum@flumos.com.au</span>
      </li>
      <li class="contact-item">
        <svg class="contact-icon" viewBox="0 0 34 22" fill="none" stroke="#1fa8e8" stroke-width="1.4">
          <circle cx="11" cy="11" r="9.5"/>
          <path d="M21 11h12M33 3v16"/>
          <circle cx="11" cy="11" r="5.5" stroke-width="1.1"/>
          <ellipse cx="11" cy="11" rx="2.3" ry="5.5" stroke-width="1"/>
          <path d="M5.5 11h11M6.5 8.2h9M6.5 13.8h9" stroke-width="0.9"/>
        </svg>
        <span class="contact-text">www.loremipsum.com</span>
      </li>
      <li class="contact-item">
        <svg class="contact-icon" viewBox="0 0 34 22" fill="none" stroke="#1fa8e8" stroke-width="1.4">
          <circle cx="11" cy="11" r="9.5"/>
          <path d="M21 11h12M33 3v16"/>
          <path d="M11 17c-2.6-3.2-4-5.4-4-7.2a4 4 0 0 1 8 0c0 1.8-1.4 4-4 7.2z" fill="#1fa8e8" stroke="none"/>
          <circle cx="11" cy="9.8" r="1.5" fill="#0a1428" stroke="none"/>
        </svg>
        <span class="contact-text">lorem ipsum dolor sit amet</span>
      </li>
    </ul>

    <div class="back-brand">
      <span class="brand-name">Flumo's</span>
    </div>
  </section>

</main>
</body>
</html>
```